Website for Strategy and proejct Management Business Advisory Firm

Create a new a fresh design to replace my existing website (www.kvrm48.com). We have a business advisory firm specializing in strategic planning, project management, and business process development among other things.

I would like to move away from narrative content and make the site seem more infographic in nature. No stock photos and more custom desinged images.

The result would be a site that is easy to navigate, content that is easy to consume, and overall leaves the viewer with a positive experience.

Our logo is black and red and I like blues and whites as well. Happy to review other color schemes though.

It would basically be a brochure site, but I would like to be able post news or a blog capability.

Our current site is hosted with HostMoxie. I would need the files necessary to stand up the site in their environment. Ideally, the designer could handle this for me as I do not have expertise in this area.

Some questions I have - will I be able to update content? Can I make revisions during the design process?

Thank you!!

Target Market(s)

Mostly small to medium size businesses although the planning framework I use and the project management methodology applies to any business segment, both for and not for profit.

Industry/Entity Type

Consulting

Coding

Coded - Design and coding required

Number of Pages Required

5+ page

Font styles to use
Sans Serif

Colors
85acd3
3277b5
0355a3
f04a50
ec1f27
0393ce

Requirements
Must have
• Infograph or icon driven look and feel. Professional yet elegant. Pages that address the nature of the company, the services we offer, brief testimonials, display logos of clients and an ability to post news or blog content.
Nice to have
• Perhaps something that is on the cool/fun side.
Should not have
• A lot of text, stock photos, broken links, content that cannot be edited easily.

```html
<!DOCTYPE html>
<html lang="en">
<head>
<meta charset="utf-8">
<title>Blue Harbor Strategic Partners</title>
<link href="https://fonts.googleapis.com/css2?family=Montserrat:wght@500;600;700&family=Didact+Gothic&display=swap" rel="stylesheet">
<style>
  :root {
    --red: #ec1f27;
    --red-soft: #f04a50;
    --ink: #1e1e1e;
    --muted: #6b6b6b;
    --white: #ffffff;
    --art-warm: #f3d9cf;
    --avatar: #d9dde2;
  }
  * { box-sizing: border-box; margin: 0; padding: 0; }
  html, body { width: 1200px; height: 2756px; overflow: hidden; }
  body {
    position: relative;
    background: var(--white);
    color: var(--ink);
    font-family: "Didact Gothic", "Century Gothic", sans-serif;
  }
  .abs { position: absolute; }

  /* Header */
  .brand { left: 80px; top: 64px; font-family: "Montserrat", sans-serif; font-weight: 600; font-size: 18px; color: var(--ink); white-space: nowrap; }
  .nav { left: 578px; top: 66px; display: flex; gap: 30px; font-family: "Montserrat", sans-serif; font-size: 14px; font-weight: 500; color: var(--ink); }
  .nav .current { color: var(--red); }
  .nav-cta { left: 990px; top: 56px; width: 146px; height: 40px; border: 2px solid var(--red); border-radius: 20px; color: var(--red); font-family: "Montserrat", sans-serif; font-size: 13px; font-weight: 600; display: flex; align-items: center; justify-content: center; }

  /* Shared */
  .btn { height: 50px; border-radius: 25px; background: var(--red); color: var(--white); font-family: "Montserrat", sans-serif; font-weight: 700; font-size: 14px; letter-spacing: 1px; display: flex; align-items: center; justify-content: center; box-shadow: 0 6px 12px rgba(236,31,39,.3); }
  .section-title { left: 0; width: 1200px; text-align: center; font-family: "Montserrat", sans-serif; font-weight: 600; font-size: 46px; color: var(--red); }
  .section-title::after { content: ""; display: block; width: 150px; height: 4px; background: var(--red); margin: 6px auto 0; }
  .body-copy { font-size: 16.5px; line-height: 1.72; color: var(--ink); }
  .art { border-radius: 16px; }

  /* Hero */
  .hero-title { left: 78px; top: 192px; width: 600px; font-family: "Montserrat", sans-serif; font-weight: 600; font-size: 47px; line-height: 1.17; color: var(--red); }
  .hero-text { left: 78px; top: 330px; width: 610px; }
  .hero-btn { left: 78px; top: 478px; width: 222px; }
  .hero-art { left: 710px; top: 215px; width: 400px; height: 275px; background: radial-gradient(circle at 50% 55%, var(--art-warm), #fbeee9 70%, var(--white)); }

  /* What we do */
  .what-title { top: 724px; }
  .service-title { left: 78px; top: 876px; font-family: "Montserrat", sans-serif; font-weight: 700; font-size: 36px; line-height: 1.18; color: var(--red); }
  .service-text { left: 78px; top: 980px; width: 600px; font-size: 15.5px; }
  .service-art { left: 690px; top: 890px; width: 420px; height: 340px; background: linear-gradient(135deg, #d6ecd0, #f5e6b8 50%, #f3c9cb); }
  .dots { left: 80px; top: 1255px; display: flex; gap: 10px; }
  .dots span { width: 22px; height: 22px; border-radius: 50%; border: 2px solid var(--red); }
  .dots .on { background: var(--red); }

  /* Partners */
  .partners-title { top: 1414px; }
  .avatar { width: 142px; height: 142px; border-radius: 50%; background: var(--avatar); top: 1532px; }
  .partner-name { top: 1700px; font-family: "Montserrat", sans-serif; font-weight: 700; font-size: 36px; color: var(--red); }
  .partner-text { top: 1762px; width: 455px; font-size: 15.5px; }
  .partner-btn { top: 1972px; width: 168px; font-size: 13px; }

  /* Contact */
  .contact { left: 0; top: 2122px; width: 1200px; height: 568px; background: var(--red); color: var(--white); }
  .contact-title { left: 78px; top: 62px; font-family: "Montserrat", sans-serif; font-weight: 600; font-size: 41px; }
  .label { font-family: "Montserrat", sans-serif; font-weight: 700; font-size: 13px; }
  .field { border: 2px solid var(--white); }
  .submit { left: 78px; top: 464px; width: 170px; height: 46px; border-radius: 23px; background: var(--white); color: var(--ink); font-family: "Montserrat", sans-serif; font-weight: 700; font-size: 15px; letter-spacing: 1px; display: flex; align-items: center; justify-content: center; }
  .info { left: 850px; font-family: "Montserrat", sans-serif; font-weight: 700; font-size: 13px; line-height: 1.5; }
</style>
</head>
<body>

<header>
  <div class="abs brand">Blue Harbor Strategic Partners</div>
  <nav class="abs nav">
    <span class="current">HOME</span><span>ABOUT US</span><span>SERVICES</span><span>TESTIMONIALS</span>
  </nav>
  <div class="abs nav-cta">CONTACT US</div>
</header>

<section class="hero">
  <h1 class="abs hero-title">Strategy and Execution Excellence</h1>
  <p class="abs hero-text body-copy">Blue Harbor Strategic Partners is a strategy and planning consulting firm which leverages practical, effective, and simple planning techniques to design business strategies and execution frameworks.</p>
  <div class="abs btn hero-btn">FIND OUT HOW</div>
  <div class="abs art hero-art" role="img" aria-label="Illustration of a team meeting around a table with papers and briefcases"></div>
</section>

<section class="what">
  <h2 class="abs section-title what-title">What We Do</h2>
  <h3 class="abs service-title">STRATEGY<br>MANAGEMENT</h3>
  <p class="abs service-text body-copy">Mission, Vision, Objectives – standards of strategic planning. Important, yes, but defining your plan does not have to be painful and time consuming. We facilitate and develop enterprise and operational business strategies using proven techniques that save time, money and add value with an emphasis on execution excellence. Our practices will help you establish actionable plans aligned with your organizations capabilities and culture. Complimented with a planning and communication rhythm, your plans stay current and your team stays informed.</p>
  <div class="abs art service-art" role="img" aria-label="Illustration of people assembling large coloured jigsaw puzzle pieces"></div>
  <div class="abs dots"><span class="on"></span><span></span><span></span><span></span><span></span></div>
</section>

<section class="partners">
  <h2 class="abs section-title partners-title">Trusted Partners</h2>

  <div class="abs avatar" style="left:88px" role="img" aria-label="Portrait of Daniel Marsh"></div>
  <h3 class="abs partner-name" style="left:78px">DANIEL MARSH</h3>
  <p class="abs partner-text body-copy" style="left:78px">Daniel Marsh is a founding partner of Blue Harbor Strategic Partners – a strategy and planning consultancy. He is responsible for facilitating the development of corporate and business strategies for his clients. Further, Daniel develops and implements execution frameworks to help his clients realize their vision and goals.</p>
  <div class="abs btn partner-btn" style="left:78px">READ MORE</div>

  <div class="abs avatar" style="left:672px" role="img" aria-label="Portrait of Lucas Brennholt"></div>
  <h3 class="abs partner-name" style="left:668px">LUCAS BRENNHOLT</h3>
  <p class="abs partner-text body-copy" style="left:668px">Lucas Brennholt is Co-Founder of BHSP where he works with organizations to develop practical strategies and supporting execution models. Through the use of a variety of proven tools, methodologies and professional facilitation techniques, BHSP has helped multiple organizations define their mission and objectives and the means for achieving them.</p>
  <div class="abs btn partner-btn" style="left:668px">READ MORE</div>
</section>

<section class="abs contact">
  <h2 class="abs contact-title">CONTACT US</h2>
  <div class="abs label" style="left:78px;top:150px">NAME *</div>
  <div class="abs field" style="left:78px;top:175px;width:285px;height:50px"></div>
  <div class="abs label" style="left:420px;top:150px">EMAIL ADDRESS *</div>
  <div class="abs field" style="left:420px;top:175px;width:285px;height:50px"></div>
  <div class="abs label" style="left:78px;top:272px">MESSAGE</div>
  <div class="abs field" style="left:78px;top:300px;width:622px;height:136px"></div>
  <div class="abs submit">SUBMIT</div>

  <svg class="abs" style="left:850px;top:130px" width="36" height="48" viewBox="0 0 24 32" aria-hidden="true"><path d="M12 0C5.4 0 0 5.4 0 12c0 9 12 20 12 20s12-11 12-20C24 5.4 18.6 0 12 0zm0 17a5 5 0 1 1 0-10 5 5 0 0 1 0 10z" fill="#fff"/></svg>
  <div class="abs info" style="top:200px">PO BOX 5210<br>LAKEPORT, MI 49012<br>U.S.A.</div>
  <svg class="abs" style="left:850px;top:305px" width="44" height="44" viewBox="0 0 24 24" aria-hidden="true"><path d="M6.6 10.8a15.2 15.2 0 0 0 6.6 6.6l2.2-2.2a1 1 0 0 1 1-.25 11.4 11.4 0 0 0 3.6.57 1 1 0 0 1 1 1V20a1 1 0 0 1-1 1A17 17 0 0 1 3 4a1 1 0 0 1 1-1h3.5a1 1 0 0 1 1 1c0 1.25.2 2.45.57 3.57a1 1 0 0 1-.25 1z" fill="#fff"/></svg>
  <div class="abs info" style="top:380px">555 018 2406</div>
</section>

</body>
</html>
```